Stationery for a private security company, "Tavrel Security Services Ltd."

Needed is a stationery design for a private security company. The designs must show professionalism and that our company mean nothing but business. Watermark of the company logo on the letterhead page is also a must. The final design must represent innovation and professionalism. It would be great if designers could integrate the colours black and silver onto the cards and letterheads..

Thank you

```html
<!DOCTYPE html>
<html lang="en">
<head>
<meta charset="utf-8">
<title>Tavrel Security Services Ltd. — Stationery</title>
<link rel="stylesheet" href="https://fonts.googleapis.com/css2?family=Montserrat:wght@500;600&display=swap">
<style>
  :root {
    --ink: #1c1c1c;
    --ink-soft: #3a3a3a;
    --paper: #ffffff;
    --silver: #e4e4e4;
    --silver-dark: #b5b5b5;
    --watermark-paper: #ececec;
    --watermark-card: #d5d5d5;
    --backdrop: #f2f2f2;
  }
  * { box-sizing: border-box; margin: 0; padding: 0; }
  html, body { width: 1200px; height: 1000px; overflow: hidden; }
  body {
    background: var(--backdrop);
    font-family: "Montserrat", sans-serif;
    color: var(--ink);
    position: relative;
  }

  .brand {
    font-weight: 600;
    text-transform: uppercase;
    letter-spacing: 0.12em;
    color: var(--ink);
    display: flex;
    align-items: center;
    gap: 8px;
    white-space: nowrap;
  }
  .brand-mark { width: 10px; height: 10px; background: var(--ink); }

  /* Name watermark: invented name set large in one faint colour and weight */
  .name-watermark {
    position: absolute;
    font-weight: 600;
    text-transform: uppercase;
    letter-spacing: 0.08em;
    line-height: 1.1;
    white-space: nowrap;
  }

  /* Letterhead */
  .letterhead {
    position: absolute;
    left: 60px; top: 50px;
    width: 636px; height: 900px;
    background: var(--paper);
    box-shadow: 0 2px 10px rgba(0,0,0,0.08);
    overflow: hidden;
  }
  .letterhead .brand {
    position: absolute; top: 60px; left: 0; right: 0;
    justify-content: center; font-size: 13px;
  }
  .letterhead .name-watermark {
    left: 34px; bottom: 40px;
    font-size: 44px;
    color: var(--watermark-paper);
  }
  .letterhead-contact {
    position: absolute; right: 44px; bottom: 250px;
    text-align: right;
    font-size: 8px; font-weight: 500;
    letter-spacing: 0.1em; line-height: 1.7;
    text-transform: uppercase;
    color: var(--ink-soft);
  }
  .label { color: var(--silver-dark); }

  /* Business cards */
  .card {
    position: absolute;
    left: 750px;
    width: 400px; height: 229px;
    background: var(--silver);
    box-shadow: 0 2px 8px rgba(0,0,0,0.1);
    overflow: hidden;
  }
  .card-front { top: 180px; }
  .card-back { top: 500px; }
  .card .name-watermark { color: var(--watermark-card); text-align: right; }
  .card-front .name-watermark { right: 22px; top: 20px; font-size: 24px; }
  .card-back .name-watermark { right: 20px; bottom: 16px; font-size: 16px; }
  .card-front .brand {
    position: absolute; left: 36px; bottom: 48px; font-size: 15px;
  }
  .card-back .brand {
    position: absolute; right: 24px; top: 22px; font-size: 10px;
  }
  .card-details {
    position: absolute; left: 26px; top: 78px;
    font-size: 8px; font-weight: 500;
    letter-spacing: 0.08em; line-height: 1.7;
    text-transform: uppercase; color: var(--ink-soft);
  }
  .card-web { margin-bottom: 12px; }
  .card-name { font-size: 11px; font-weight: 600; color: var(--ink); }
  .card-role { margin-bottom: 12px; }
</style>
</head>
<body>

<section class="letterhead">
  <div class="brand"><span class="brand-mark"></span>Tavrel Security Services Ltd.</div>
  <div class="name-watermark" aria-hidden="true">Tavrel<br>Security<br>Services Ltd.</div>
  <div class="letterhead-contact">
    <p>&gt;&gt;&gt; info@tavrelsecurity.co.uk</p>
    <p><span class="label">| Phone |</span> +44 800 555 0142 <span class="label">| Fax |</span> +44 800 555 0143</p>
    <p>Kestrel House | 22 Alder Road</p>
    <p>Thornbury | Westshire | TB4 7QZ</p>
  </div>
</section>

<section class="card card-front">
  <div class="name-watermark" aria-hidden="true">Tavrel<br>Security<br>Services Ltd.</div>
  <div class="brand"><span class="brand-mark"></span>Tavrel Security Services Ltd.</div>
</section>

<section class="card card-back">
  <div class="name-watermark" aria-hidden="true">Tavrel<br>Security<br>Services Ltd.</div>
  <div class="brand"><span class="brand-mark"></span>Tavrel Security Services Ltd.</div>
  <div class="card-details">
    <p class="card-web">&gt;&gt;&gt; www.tavrelsecurity.co.uk</p>
    <p class="card-name">Marcus Hale</p>
    <p class="card-role">[Director]</p>
    <p>mhale@tavrelsecurity.co.uk</p>
    <p><span class="label">| Phone |</span> +44 800 555 0142</p>
    <p><span class="label">| Fax |</span> +44 800 555 0143</p>
    <p>Kestrel House | 22 Alder Road</p>
    <p>Thornbury | Westshire | TB4 7QZ</p>
  </div>
</section>

</body>
</html>
```